bluegate mental health stationary

Please help turn this logo into a total image for my business.
Stationary need to be able to be individualized for each mental health practitioners

Some generic info about services
Clinical Psychology - Consultant Psychiatry - Locum Services - Medico-legal - Architectural Adviser Clinical and Medical Facilities

Target Market(s)

Letter head for doctors, courts, patients.

Industry/Entity Type

Mental Health

Requirements
Must have
• area where practitioners details can be listed and logo on page
Nice to have
• embossed section

```html
<!DOCTYPE html>
<html lang="en">
<head>
<meta charset="utf-8">
<title>Bluegate Mental Health — Letterhead</title>
<link href="https://fonts.googleapis.com/css2?family=Raleway:wght@400;500;600&family=Tinos:ital,wght@0,400;0,700;1,400&display=swap" rel="stylesheet">
<style>
  :root {
    --backdrop: #e4e5e7;
    --paper: #ffffff;
    --navy: #1c4466;
    --slate: #34506b;
    --mark-grey: #8a9097;
    --ink: #2a2a2a;
    --muted: #5d6670;
    --rule: #9aa3ab;
    --band-text: #ffffff;
  }
  * { box-sizing: border-box; margin: 0; padding: 0; }
  html, body {
    width: 1200px; height: 909px; overflow: hidden;
    background: var(--backdrop);
  }
  .letterhead {
    position: absolute; left: 296px; top: 24px;
    width: 608px; height: 860px;
    background: var(--paper);
    box-shadow: 0 2px 10px rgba(0,0,0,.12);
    overflow: hidden;
    font-family: "Tinos", "Times New Roman", serif;
    color: var(--ink);
  }
  .brand {
    position: absolute; left: 40px; top: 46px;
    display: flex; align-items: center; gap: 10px;
  }
  .brand-square { width: 30px; height: 30px; background: var(--mark-grey); }
  .brand-name {
    font-family: "Raleway", Arial, sans-serif; font-weight: 500;
    color: var(--slate); line-height: 1;
  }
  .brand-name .primary { display: block; font-size: 24px; letter-spacing: 1px; text-transform: uppercase; }
  .brand-name .secondary { display: block; font-size: 9px; letter-spacing: 2.4px; text-transform: uppercase; margin-top: 3px; }
  .practitioner {
    position: absolute; left: 40px; top: 98px; width: 528px;
    font-family: "Raleway", Arial, sans-serif; font-size: 7px; color: var(--muted);
    border-top: 1px solid var(--rule); padding-top: 5px; line-height: 1.5;
  }
  .practitioner strong { color: var(--ink); font-weight: 600; }
  .contact {
    position: absolute; left: 330px; top: 40px;
    font-family: "Raleway", Arial, sans-serif; font-size: 7.5px; color: var(--muted); line-height: 1.7;
  }
  .contact .row { display: flex; gap: 14px; }
  .contact .icon { color: var(--navy); font-weight: 600; margin-right: 3px; }
  .contact strong { color: var(--ink); }
  .letter {
    position: absolute; left: 40px; top: 160px; width: 528px;
    font-size: 10.5px; line-height: 1.45; text-align: justify;
  }
  .letter p { margin-bottom: 12px; }
  .closing { position: absolute; left: 40px; top: 520px; font-size: 10.5px; line-height: 1.45; }
  .signature-area { width: 90px; height: 30px; margin: 6px 0 2px; background: linear-gradient(90deg, #eceef0, #f7f7f8); }
  .signer { font-weight: 700; }
  .service-band {
    position: absolute; left: 0; bottom: 0; width: 100%; height: 140px;
    background: var(--navy);
    display: flex; flex-direction: column; justify-content: flex-end; align-items: flex-end;
    padding: 0 26px 24px;
    font-family: "Raleway", Arial, sans-serif; color: var(--band-text);
    font-size: 11px; letter-spacing: .3px; line-height: 1.6; text-align: right;
  }
</style>
</head>
<body>
  <main class="letterhead">
    <div class="brand">
      <span class="brand-square"></span>
      <span class="brand-name"><span class="primary">Bluegate</span><span class="secondary">Mental Health</span></span>
    </div>

    <address class="contact">
      <div>24 Larkspur Close, ELMVALE 6107</div>
      <div class="row"><span><span class="icon">T</span>(08) 9310 4862</span><span><span class="icon">M</span>0491 286 075</span></div>
      <div><span class="icon">E</span>mholt@bgmh.example</div>
      <div><strong>ABN:</strong> 41 602 118 954 <strong>ACN:</strong> 148220736</div>
    </address>

    <div class="practitioner">
      <strong>Maren Holt</strong> M. Psych (Clinical), M. Genetic Couns., B.A. (Psych) &nbsp;Reg. no: PSY0004418273 Provider no: 5830264T<br>
      Member of the Coastal Psychology Society
    </div>

    <article class="letter">
      <p>Gentlemen,</p>
      <p>Enclosed I have the honor to send you an article which I should be pleased if you would accept for the "Harbour Quarterly". I am <em>desperately</em> pushed for money; and in the event of Mr. Farrell's liking the "Landscape-Garden", I would take it as an especial favor if you would mail me the amount due for it, so as to reach me here by the 21st, on which day I shall need it. Can you possibly oblige me in this? If you accept the paper I presume you will allow me your usual sum, whatever that is for similar contributions—but I set no price—leaving all to your own liberality. The piece will make 8 of your pages and rather more.</p>
      <p>Will you be kind enough to put the best possible interpretation upon my behavior while in N-York? You must have conceived a <em>queer</em> idea of me—but the simple truth is that Linton would insist upon <em>the juleps</em>, and I knew not what I was either doing or saying. The Review of Merrow which I offered you was deficient in a 1/2 page of commencement, which I had written to supersede the old beginning, and which gave the article the character of a general and retrospective review. No wonder you did not take it—I would have been very much mortified if you had. I hope to see you at some future time, under better auspices.</p>
    </article>

    <div class="closing">
      <div>In the meantime I remain</div>
      <div>Yours very truly,</div>
      <div class="signature-area" role="img" aria-label="Handwritten signature"></div>
      <div class="signer">Edwin A. Marsh</div>
    </div>

    <footer class="service-band">
      <div>Clinical Psychology - Consultant Psychiatry - Locum Services - Medico-legal</div>
      <div>Architectural Adviser Clinical and Medical Facilities</div>
    </footer>
  </main>
</body>
</html>
```